Mexican construction company needs a business card design

We need a business card design for a company based in Monterrey, Mexico called:

Desarrollos Quilbeta S.A. de C.V.

The company is in the construction business and I would like the businees card to be simple and concise. Please use white background and blue or black text color that say:

"Proyectos de Construcción"-- (Brief description of business)
" Rodrigo Velun Osorio"--- (My name)
"rvelun@correoplat.mx"-- (My email)
"C: (81) 52 19 67 43"-- (My cell)
"O: (81) 56 72 18 94"-- (Office phone)

Please use only the colors of my company that are attached

Please make the back of the business card blue (same blue from logo) and use the logo.

Thanks!

```html
<!DOCTYPE html>
<html lang="es">
<head>
<meta charset="utf-8">
<title>Desarrollos Quilbeta – Tarjeta de presentación</title>
<link rel="stylesheet" href="https://fonts.googleapis.com/css2?family=Fira+Sans:wght@400;500&family=Fira+Sans+Condensed:wght@400;500&display=swap">
<style>
  :root {
    --backdrop: #a9a7a9;
    --navy: #24214a;
    --silver: #a2a2a4;
    --paper: #ffffff;
    --ink: #2a2a33;
    --icon: #c9c9cf;
  }
  * { margin: 0; padding: 0; box-sizing: border-box; }
  html, body {
    width: 1200px; height: 1200px; overflow: hidden;
    background: var(--backdrop);
    font-family: "Fira Sans", Arial, sans-serif;
  }
  .card {
    position: absolute;
    border-radius: 26px;
    overflow: hidden;
  }
  .card--back {
    left: 238px; top: 118px; width: 712px; height: 420px;
    background: var(--navy);
  }
  .card--front {
    left: 232px; top: 645px; width: 710px; height: 415px;
    background: var(--paper);
  }
  .brand {
    position: absolute;
    display: flex; align-items: center; gap: 22px;
  }
  .brand__mark {
    width: 58px; height: 58px;
    background: var(--silver);
  }
  .brand__name {
    font-family: "Fira Sans", Arial, sans-serif;
    font-weight: 500;
    text-transform: uppercase;
    letter-spacing: 3px;
    line-height: 1.05;
  }
  .brand__name span { display: block; }
  .card--back .brand { left: 150px; top: 150px; }
  .card--back .brand__name { color: var(--paper); font-size: 34px; }
  .card--front .brand { left: 46px; top: 78px; }
  .card--front .brand__name { color: var(--navy); font-size: 36px; }
  .swoosh { position: absolute; left: 0; top: 0; }
  .tagline {
    position: absolute; left: 43px; top: 236px;
    font-size: 18px; color: var(--ink); font-weight: 400;
  }
  .holder {
    position: absolute; left: 43px; top: 270px;
    font-family: "Fira Sans Condensed", Arial, sans-serif;
    font-size: 22px; font-weight: 500; color: var(--navy);
  }
  .contact {
    position: absolute; right: 38px; top: 300px;
    list-style: none;
    color: var(--paper);
    font-family: "Fira Sans Condensed", Arial, sans-serif;
    font-size: 17px;
  }
  .contact li {
    display: flex; justify-content: flex-end; align-items: center;
    gap: 12px; height: 26.5px;
  }
  .contact svg { width: 18px; height: 16px; fill: var(--icon); }
</style>
</head>
<body>

<section class="card card--back" aria-label="Reverso de la tarjeta">
  <div class="brand">
    <div class="brand__mark"></div>
    <div class="brand__name"><span>Desarrollos</span><span>Quilbeta</span></div>
  </div>
</section>

<section class="card card--front" aria-label="Frente de la tarjeta">
  <div class="brand">
    <div class="brand__mark"></div>
    <div class="brand__name"><span>Desarrollos</span><span>Quilbeta</span></div>
  </div>

  <svg class="swoosh" width="710" height="415" viewBox="0 0 710 415" aria-hidden="true">
    <path fill="var(--navy)" d="M0 415 L0 340 C160 395 400 365 540 250 C610 195 665 188 710 185 L710 415 Z"/>
    <path fill="var(--silver)" d="M60 322 C260 372 440 330 560 225 C620 175 670 165 710 160 L710 178 C665 182 615 195 550 245 C430 345 250 370 60 322 Z"/>
    <path fill="var(--paper)" d="M50 338 C260 385 450 350 570 250 C630 205 675 195 710 192 L710 200 C670 205 630 215 575 260 C455 360 260 390 50 338 Z"/>
    <path fill="var(--silver)" d="M0 378 C120 392 220 392 330 372 C220 400 110 402 0 395 Z"/>
  </svg>

  <p class="tagline">Proyectos de Construcción</p>
  <p class="holder">Rodrigo Velun Osorio</p>

  <ul class="contact">
    <li>(81) 56 72 18 94
      <svg viewBox="0 0 18 16" aria-hidden="true"><path d="M2 5 C2 2 5 1 9 1 C13 1 16 2 16 5 L13 6 L12 4 C10 3.5 8 3.5 6 4 L5 6 Z M4 8 L14 8 L16 15 L2 15 Z"/></svg>
    </li>
    <li>(81) 52 19 67 43
      <svg viewBox="0 0 18 16" aria-hidden="true"><path d="M5 0 H13 V16 H5 Z M6.5 2 V12 H11.5 V2 Z"/></svg>
    </li>
    <li>rvelun@correoplat.mx
      <svg viewBox="0 0 18 16" aria-hidden="true"><path d="M1 3 H17 V13 H1 Z M2.5 4 L9 9 L15.5 4 Z"/></svg>
    </li>
  </ul>
</section>

</body>
</html>
```